Website design for staffing/workforce solutions company - Halvard Staffing Solutions

Create a launch-ready website
Halvard Staffing Solutions also known as HSS. This is a company that specializes in Staffing/Work force solutions for Healthcare/IT/Logistics/Maintenance/Construction/Manufacturing/Industrial/General Labor. HSS works with government agencies/contracts also. Use the attached logo in the build of the website. Website should be clean, modern, engaging, innovative. Website needs to speak to the professional services industry.
Halvard Staffing Solutions or HSS is a certified VOSB, SDVOSB, DBE and Minority-Owned Business.
The website needs to be compliant for government contracting.

Website needs to include the following--
Modern UI/UX Enhancements: A hero section with a strong call-to-action.
Government Contracting Compliance: Certification display and a Capability Statement download.
Advanced Careers Section: A dedicated job application portal.
Social Media & Lead Generation: Links to Profilary, Quillo, and Mingleo.
Security & Performance: Optimized for SEO, fast loading, and mobile responsiveness.
1. Modern Design Upgrades
๐Ÿ”น Upgrade UI/UX for a Professional, Trustworthy Look
โœ… Full-width hero banner with a high-quality background image representing business, technology, and workforce solutions.
โœ… Animated elements (subtle transitions for smooth browsing experience).
โœ… Bold CTA buttons for easy navigation to key actions (e.g., โ€œGet Startedโ€ or โ€œRequest a Consultationโ€).
โœ… Dark-themed header with contrasting colors (professional & government-trustworthy).
โœ… New Homepage Hero Section Example:
"Your Trusted Partner in Workforce, IT, Maintenance & Logistics Solutions"
Button: "Discover Our Services"

2. Enhanced Government Contracting Section (Key for Compliance)
๐Ÿ“Œ Essential for securing contracts & building credibility
โœ… Capability Statement (Downloadable PDF)

Showcase key past contracts, company qualifications, and services in a downloadable format for government buyers.
โœ… Certifications Display (VOSB, SDVOSB, DBE, Minority-Owned Business)

Visual badge display to emphasize legitimacy for government contracts.
โœ… Procurement Readiness Details

NAICS Codes, DUNS Number, CAGE Code, and relevant VPR.example registration details.
โœ… Past Performance Showcase (Case Studies Section)

Highlight successful projects and government contracts.
โœ… Compliance & Security

Add SOC 2, HIPAA (for healthcare staffing), and ITAR compliance if applicable.
3. Advanced Job Search & Candidate Portal (For Staffing Services)
๐Ÿ“Œ To attract top talent for staffing contracts

โœ… Advanced Job Search Feature

Filters: Industry, location, job type (contract/full-time), salary range, and clearance level (for government jobs).
โœ… Candidate Login Portal

Applicants can upload resumes, track applications, and receive job alerts.
โœ… Employer Portal (For Businesses Hiring Through HSS)

A dedicated section for companies to submit staffing requests and view candidate matches.
4. Service-Specific Landing Pages (SEO & Engagement)
๐Ÿ“Œ Helps different industries find relevant services faster

๐Ÿ”น Dedicated Pages for Each Service:
โœ… Staffing & Workforce Solutions

Specialized sections for Healthcare, IT, Construction, Industrial, and General Labor staffing.
โœ… IT Services

List services like Cybersecurity, Cloud Solutions, and IT Consulting.
Showcase tech stack & certifications.
โœ… Logistics & Maintenance

Detail fleet management, supply chain services, and industrial maintenance.
โœ… Government Contracting Solutions

A streamlined page for government agencies.
5. Security & Compliance Upgrades (For Government Work)
๐Ÿ“Œ To ensure compliance & credibility in government contracting

โœ… SSL Certification (100% Required for Security)

Secure client and job applicant data.
โœ… ADA Compliance (Accessibility)

Ensure the website follows WCAG 2.1 accessibility standards for government clients.
โœ… GDPR & Data Protection Features

A privacy policy and terms of service to comply with data regulations.
6. Performance & Mobile Optimization
๐Ÿ“Œ To ensure fast loading & responsiveness

โœ… Mobile-Responsive Design

Optimized for mobile-friendly navigation since many users browse from phones.
โœ… Fast-Loading Pages

Optimize images & implement lazy loading for better site speed.
โœ… SEO-Optimized Pages

Improve search ranking on Searvo with:
Keyword-optimized content (e.g., โ€œGovernment Contracting Staffing Servicesโ€)
Schema markup for job listings
Blog/articles about staffing trends
7. Social Media & Lead Generation
๐Ÿ“Œ For brand credibility & client engagement

โœ… Profilary, Quillo, Mingleo Integration

Display recent updates from Profilary (primary for B2B & government).
โœ… Lead Capture Forms

Forms for business inquiries, talent applications, and government RFPs.
โœ… Client & Candidate Testimonials
Showcase client success stories & employee experiences

Good websites to pull examples for inspiration/direction--
https://www.pelmora.example/
https://www.tovrinex.example/
https://brambleworks.example/homepage/
https://www.quantelvetting.example/capability-statement

Staffing/Professional Services

Coded - Design and coding required

5+ page

• Website needs to include the following-- Modern UI/UX Enhancements: A hero section with a strong call-to-action. Government Contracting Compliance: Certification display and a Capability Statement download. Advanced Careers Section: A dedicated job application portal. Social Media & Lead Generation: Links to Profilary, Quillo, and Mingleo. Security & Performance: Optimized for SEO, fast loading, and mobile responsiveness. 1. Modern Design Upgrades ๐Ÿ”น Upgrade UI/UX for a Professional, Trustworthy Look โœ… Full-width hero banner with a high-quality background image representing business, technology, and workforce solutions. โœ… Animated elements (subtle transitions for smooth browsing experience). โœ… Bold CTA buttons for easy navigation to key actions (e.g., โ€œGet Startedโ€ or โ€œRequest a Consultationโ€). โœ… Dark-themed header with contrasting colors (professional & government-trustworthy). โœ… New Homepage Hero Section Example: "Your Trusted Partner in Workforce, IT, & Logistics Solutions" Button: "Discover Our Services" 2. Enhanced Government Contracting Section (Key for Compliance) ๐Ÿ“Œ Essential for securing contracts & building credibility โœ… Capability Statement (Downloadable PDF) Showcase key past contracts, company qualifications, and services in a downloadable format for government buyers. โœ… Certifications Display (VOSB, SDVOSB, DBE, Minority-Owned Business) Visual badge display to emphasize legitimacy for government contracts. โœ… Procurement Readiness Details NAICS Codes, DUNS Number, CAGE Code, and relevant VPR.example registration details. โœ… Past Performance Showcase (Case Studies Section) Highlight successful projects and government contracts. โœ… Compliance & Security Add SOC 2, HIPAA (for healthcare staffing), and ITAR compliance if applicable. 3. Advanced Job Search & Candidate Portal (For Staffing Services) ๐Ÿ“Œ To attract top talent for staffing contracts โœ… Advanced Job Search Feature Filters: Industry, location, job type (contract/full-time), salary range, and clearance level (for government jobs). โœ… Candidate Login Portal Applicants can upload resumes, track applications, and receive job alerts. โœ… Employer Portal (For Businesses Hiring Through HSS) A dedicated section for companies to submit staffing requests and view candidate matches. 4. Service-Specific Landing Pages (SEO & Engagement) ๐Ÿ“Œ Helps different industries find relevant services faster ๐Ÿ”น Dedicated Pages for Each Service: โœ… Staffing & Workforce Solutions Specialized sections for Healthcare, IT, Construction, Industrial, and General Labor staffing. โœ… IT Services List services like Cybersecurity, Cloud Solutions, and IT Consulting. Showcase tech stack & certifications. โœ… Logistics & Maintenance Detail fleet management, supply chain services, and industrial maintenance. โœ… Government Contracting Solutions A streamlined page for government agencies. 5. Security & Compliance Upgrades (For Government Work) ๐Ÿ“Œ To ensure compliance & credibility in government contracting โœ… SSL Certification (100% Required for Security) Secure client and job applicant data. โœ… ADA Compliance (Accessibility) Ensure the website follows WCAG 2.1 accessibility standards for government clients. โœ… GDPR & Data Protection Features A privacy policy and terms of service to comply with data regulations. 6. Performance & Mobile Optimization ๐Ÿ“Œ To ensure fast loading & responsiveness โœ… Mobile-Responsive Design Optimized for mobile-friendly navigation since many users browse from phones. โœ… Fast-Loading Pages Optimize images & implement lazy loading for better site speed. โœ… SEO-Optimized Pages Improve search ranking on Searvo with: Keyword-optimized content (e.g., โ€œGovernment Contracting Staffing Servicesโ€) Schema markup for job listings Blog/articles about staffing trends 7. Social Media & Lead Generation ๐Ÿ“Œ For brand credibility & client engagement โœ… Profilary, Quillo, Mingleo Integration Display recent updates from Profilary (primary for B2B & government). โœ… Lead Capture Forms Forms for business inquiries, talent applications, and government RFPs. โœ… Client & Candidate Testimonials Showcase client success stories & employee experiences Good websites to pull examples for inspiration/direction-- https://www.pelmora.example/ https://www.tovrinex.example/ https://brambleworks.example/homepage/

```html
<!DOCTYPE html>
<html lang="en">
<head>
<meta charset="utf-8">
<title>Halvard Staffing Solutions — Where Talent Meets Mission</title>
<link href="https://fonts.googleapis.com/css2?family=Michroma&family=DM+Sans:wght@400;500;700&display=swap" rel="stylesheet">
<style>
:root{
  --red:#e3141b;
  --red-soft:#f1c3c6;
  --ink:#101a1c;
  --panel:#0f1f22;
  --page:#f3f3fa;
  --white:#ffffff;
  --muted:#5b6266;
  --head:"Michroma",sans-serif;
  --body:"DM Sans",sans-serif;
}
*{box-sizing:border-box;margin:0;padding:0}
html,body{width:1200px;height:4616px;overflow:hidden}
body{position:relative;background:var(--page);font-family:var(--body);color:var(--ink)}
.abs{position:absolute}
a{color:inherit;text-decoration:none}
.btn{position:absolute;display:flex;align-items:center;justify-content:center;font:500 15px var(--body);border-radius:4px}
.btn-red{background:var(--red);color:var(--white)}
.section-title{position:absolute;left:0;width:1200px;text-align:center;font:400 34px var(--head);letter-spacing:2px}
.fill{position:absolute}

/* header */
.site-header{position:absolute;left:0;top:0;width:1200px;height:64px;background:var(--white);z-index:3}
.brand{position:absolute;left:72px;top:18px;font:700 20px var(--body);color:var(--ink);display:flex;align-items:center;gap:10px}
.brand i{display:block;width:14px;height:14px;background:var(--red)}
.nav{position:absolute;left:366px;top:22px;display:flex;gap:34px;font:500 15px var(--body)}
.nav .active{border-bottom:2px solid var(--red);padding-bottom:2px}

/* hero */
.hero{position:absolute;left:0;top:0;width:1200px;height:820px;background:linear-gradient(90deg,#1a1d22 0%,#3a3d44 45%,#b9b4ae 100%)}
.hero h1{position:absolute;left:72px;top:212px;width:620px;font:400 44px/64px var(--head);color:var(--white);letter-spacing:2px}
.hero p{position:absolute;left:72px;top:406px;width:560px;font:400 14px/22px var(--body);color:#e8e8ea}
.btn-white{background:var(--white);color:var(--red)}
.btn-outline{border:2px solid var(--red);color:var(--white)}
.stats{position:absolute;left:72px;top:676px;display:flex;gap:54px}
.stat b{display:block;font:400 30px var(--head);color:var(--white)}
.stat span{font:500 15px var(--body);color:var(--white);letter-spacing:1px}

/* about */
.about-panel{position:absolute;left:520px;top:924px;width:640px;height:376px;background:var(--panel);color:var(--white);padding:40px 44px}
.about-panel h2{font:400 34px var(--head);letter-spacing:2px}
.about-panel p{margin-top:22px;font:400 13px/20px var(--body);color:#d9dcdd}
.about-panel ul{list-style:none;margin-top:18px}
.about-panel li{font:400 13px/20px var(--body);color:#d9dcdd;display:flex;gap:12px;align-items:center;margin-bottom:14px}
.about-panel li::before{content:"";width:14px;height:14px;background:var(--red);flex:none}
.corner{position:absolute;width:0;height:0}
.tiny-box{position:absolute;width:26px;height:26px;border:2px solid #c9cfd2;border-radius:4px}

/* services */
.svc-card{position:absolute;top:1488px;width:346px;height:254px}
.svc-card h3{position:absolute;left:20px;top:16px;font:400 22px/28px var(--head);color:var(--white)}
.svc-card p{position:absolute;left:20px;bottom:26px;width:300px;font:400 13px/18px var(--body);color:#eee}

/* industry */
.industry{position:absolute;left:0;top:1920px;width:1200px;height:660px;background:linear-gradient(180deg,#2a2a2e 0%,#1b1c20 100%)}
.ind-card{position:absolute;top:2060px;width:344px;height:386px;background:var(--white);border-bottom:4px solid var(--red)}
.ind-card .photo{position:absolute;left:0;top:0;width:344px;height:200px}
.ind-card .icon{position:absolute;left:22px;top:172px;width:56px;height:56px;border-radius:50%;background:var(--red);border:4px solid var(--white)}
.ind-card h3{position:absolute;left:24px;top:236px;font:400 21px var(--head)}
.ind-card .rule{position:absolute;left:0;top:268px;width:344px;height:2px;background:var(--red)}
.ind-card p{position:absolute;left:24px;top:284px;width:296px;font:400 13px/20px var(--body);color:var(--muted)}

/* careers */
.careers-band{position:absolute;left:0;top:2688px;width:1200px;height:272px;background:var(--red)}
.careers-band h2{position:absolute;left:448px;top:70px;font:400 30px/40px var(--head);color:var(--white);letter-spacing:1px}
.careers-band p{position:absolute;left:448px;top:158px;width:300px;font:400 13px/19px var(--body);color:#fbe3e4}
.btn-dark{background:var(--ink);color:var(--white);font-weight:700;font-size:13px}

/* testimonials */
.quote-card{position:absolute;top:3232px;width:346px;height:290px;background:var(--white);border-bottom:4px solid var(--red);box-shadow:0 4px 14px rgba(0,0,0,.06);text-align:center}
.quote-card .mark{position:absolute;left:0;width:100%;top:18px;font:700 34px var(--body);color:var(--red)}
.quote-card p{position:absolute;left:26px;top:66px;width:294px;font:400 13px/20px var(--body);color:var(--muted)}
.quote-card .line{position:absolute;left:133px;top:140px;width:80px;height:1px;background:#ccc}
.quote-card .avatar{position:absolute;left:141px;top:168px;width:64px;height:64px;border-radius:50%;background:linear-gradient(#c9b7a4,#8e7b6a);border:3px solid var(--red-soft)}
.quote-card .name{position:absolute;left:0;width:100%;top:248px;font:500 13px var(--body)}

/* contact */
.contact-title{position:absolute;left:72px;top:3680px;font:400 34px var(--head);letter-spacing:2px}
.field{position:absolute;left:72px;width:520px;height:48px;background:var(--red-soft);padding:15px 16px;font:400 14px var(--body);color:#6b4a4d}
.info{position:absolute;left:700px;top:3740px;width:428px;height:428px;background:var(--panel);color:var(--white);padding:52px 32px}
.info h3{font:400 22px var(--head);letter-spacing:2px}
.info-row{display:flex;gap:18px;margin-top:26px}
.info-row svg{flex:none}
.info-row b{display:block;font:500 14px var(--body)}
.info-row span{font:400 13px var(--body);color:#cfd4d6}

/* footer */
.site-footer{position:absolute;left:0;top:4260px;width:1200px;height:356px;background:#111516;color:var(--white)}
.site-footer .brand{left:72px;top:58px;color:var(--white);font-size:26px}
.f-nav{position:absolute;left:590px;top:72px;display:flex;gap:40px;font:400 14px var(--body)}
.socials{position:absolute;left:72px;top:190px;display:flex;gap:26px}
.socials span{width:26px;height:26px;border-radius:50%;background:var(--white)}
.f-text{position:absolute;left:500px;top:162px;width:500px;font:400 13px/20px var(--body);color:#cfd2d3}
.f-bottom{position:absolute;left:72px;top:300px;width:1056px;display:flex;justify-content:space-between;font:400 13px var(--body);color:#cfd2d3;border-top:1px solid #333;padding-top:16px}
.f-bottom div{display:flex;gap:52px}
</style>
</head>
<body>

<section class="hero">
  <div class="fill" role="img" aria-label="Photo of a smiling professional woman with glasses at a laptop in a modern office" style="left:560px;top:0;width:640px;height:820px;background:linear-gradient(90deg,rgba(60,60,66,0) 0%,#d8d2cb 60%,#ece8e3 100%)"></div>
  <h1>WHERE TALENT MEETS MISSION</h1>
  <p>Lorem ipsum dolor sit amet consectetur. Eget mauris ac lacinia pellentesque magna. Nullam diam nulla aliquam convallis. Augue dui ut morbi lacus integer purus vitae. Eget enim sed nec nulla sit adipiscing ullamcorper.</p>
  <a class="btn btn-white" style="left:72px;top:552px;width:130px;height:50px">Contact Us</a>
  <a class="btn btn-outline" style="left:266px;top:552px;width:160px;height:50px">Contact Us</a>
  <div class="stats">
    <div class="stat"><b>100K</b><span>WORKERS</span></div>
    <div class="stat"><b>20K</b><span>CUSTOMER</span></div>
    <div class="stat"><b>50K</b><span>COMPLETE</span></div>
  </div>
</section>

<header class="site-header">
  <a class="brand"><i></i>Halvard Staffing Solutions</a>
  <nav class="nav">
    <a class="active">Home</a><a>About Us</a><a>Service</a><a>Careers</a><a>Contact</a><a>Testimonials</a>
  </nav>
  <a class="btn btn-red" style="left:960px;top:10px;width:160px;height:44px">Contact Us</a>
</header>

<section class="about">
  <div class="fill" role="img" aria-label="Photo of a team meeting around a table in a bright office" style="left:72px;top:900px;width:436px;height:420px;background:linear-gradient(160deg,#6d6a66,#3d4a54 60%,#8a7d6d)"></div>
  <div class="about-panel">
    <h2>ABOUT US</h2>
    <p>Lorem ipsum dolor sit amet consectetur. Eget mauris ac lacinia pellentesque magna. Nullam diam nulla aliquam convallis. Augue dui ut morbi lacus integer purus vitae. Eget enim sed nec nulla sit adipiscing ullamcorper.</p>
    <ul>
      <li>Lorem ipsum dolor sit amet consectetur lorem ipsum dolor sit amet consectetur.</li>
      <li>Eget mauris ac lacinia pellentesque magna eget mauris ac lacinia.</li>
      <li>Augue dui ut morbi lacus integer purus vitae augue.</li>
    </ul>
    <a class="btn" style="position:absolute;left:44px;top:312px;width:148px;height:42px;background:var(--white);color:var(--red)">Contact Us</a>
    <span class="tiny-box" style="left:212px;top:320px"></span>
    <span class="tiny-box" style="left:246px;top:320px"></span>
    <span class="tiny-box" style="left:280px;top:320px"></span>
  </div>
  <svg class="abs" style="left:1100px;top:900px" width="60" height="60" aria-hidden="true"><polygon points="0,0 60,0 60,60" fill="var(--red)"/><polygon points="0,0 60,60 0,60" fill="var(--white)"/></svg>
</section>

<section class="services">
  <h2 class="section-title" style="top:1404px">SERVICES</h2>
  <article class="svc-card" style="left:72px">
    <div class="fill" role="img" aria-label="Photo of a server room lit in blue and purple" style="inset:0;background:linear-gradient(160deg,#3b2c6a,#1a2b5c 60%,#0f1432)"></div>
    <h3>IT SERVICES</h3>
    <p>Lorem ipsum dolor sit amet consectetur. Eget mauris ac lacinia pellentesque magna.</p>
  </article>
  <article class="svc-card" style="left:428px">
    <div class="fill" role="img" aria-label="Photo of a warehouse worker in a high-visibility vest" style="inset:0;background:linear-gradient(160deg,#8a5a32,#4a3a32 60%,#2a2624)"></div>
    <h3>LOGISTICS &amp;<br>MAINTENANCE</h3>
    <p>Lorem ipsum dolor sit amet consectetur. Eget mauris ac lacinia pellentesque magna.</p>
  </article>
  <article class="svc-card" style="left:784px">
    <div class="fill" role="img" aria-label="Photo of an engineer in a hard hat reviewing a tablet on site" style="inset:0;background:linear-gradient(160deg,#7a9bb8,#5a6a72 60%,#3a3f3a)"></div>
    <h3>GOVERNMENT<br>CONTRACTING<br>SOLUTIONS</h3>
    <p>Lorem ipsum dolor sit amet consectetur. Eget mauris ac lacinia pellentesque magna.</p>
  </article>
  <a class="btn btn-red" style="left:508px;top:1786px;width:184px;height:46px">More Services</a>
</section>

<section class="industry" role="img" aria-label="Dark background photo of a crowd of business people in silhouette"></section>
<h2 class="section-title" style="top:1952px;color:var(--white)">INDUSTRY</h2>
<article class="ind-card" style="left:72px">
  <div class="photo" role="img" aria-label="Photo of doctors discussing a chart" style="background:linear-gradient(160deg,#dfe6ea,#9fb2bd)"></div>
  <span class="icon"></span>
  <h3>HOSPITAL</h3><span class="rule"></span>
  <p>Lorem ipsum dolor sit amet consectetur. Eget mauris ac lacinia pellentesque magna. Nullam diam nulla aliquam convallis.</p>
</article>
<article class="ind-card" style="left:428px">
  <div class="photo" role="img" aria-label="Photo of construction workers reviewing plans" style="background:linear-gradient(160deg,#c9b89a,#7a6a55)"></div>
  <span class="icon"></span>
  <h3>CONSTRACTION</h3><span class="rule"></span>
  <p>Lorem ipsum dolor sit amet consectetur. Eget mauris ac lacinia pellentesque magna. Nullam diam nulla aliquam convallis.</p>
</article>
<article class="ind-card" style="left:784px">
  <div class="photo" role="img" aria-label="Photo of a consultant speaking with a doctor" style="background:linear-gradient(160deg,#e3e8ec,#a4b4be)"></div>
  <span class="icon"></span>
  <h3>CANSULTING</h3><span class="rule"></span>
  <p>Lorem ipsum dolor sit amet consectetur. Eget mauris ac lacinia pellentesque magna. Nullam diam nulla aliquam convallis.</p>
</article>
<a class="btn btn-red" style="left:508px;top:2480px;width:184px;height:46px">More Services</a>

<section class="careers">
  <h2 class="section-title" style="top:2632px">CAREERS</h2>
  <div class="careers-band">
    <h2>APPLY FOR A<br>JOB WITH US</h2>
    <p>Lorem ipsum dolor sit amet consectetur. Eget mauris ac lacinia pellentesque magna. Nullam diam nulla aliquam convallis.</p>
    <a class="btn btn-dark" style="left:448px;top:208px;width:188px;height:40px">DOWNLOAD PDF &nbsp;➜</a>
  </div>
  <div class="fill" role="img" aria-label="Photo of a businesswoman holding a laptop" style="left:130px;top:2600px;width:280px;height:390px;background:linear-gradient(180deg,#3a3434,#6a5a58 50%,#2a2a30)"></div>
  <div class="fill" role="img" aria-label="Photo of a man in a blue shirt using his phone" style="left:800px;top:2640px;width:240px;height:420px;background:linear-gradient(180deg,#4a3a34,#3d5a8a 40%,#2a2e3a)"></div>
</section>

<section class="testimonials">
  <h2 class="section-title" style="top:3168px">TESTIMONIALS</h2>
  <article class="quote-card" style="left:72px"><span class="mark">“</span><p>Lorem ipsum dolor sit amet consectetur. Eget mauris ac lacinia pellentesque magna. Nullam diam nulla aliquam convallis.</p><span class="line"></span><span class="avatar" role="img" aria-label="Client portrait"></span><span class="name">Mara Quillen</span></article>
  <article class="quote-card" style="left:428px"><span class="mark">“</span><p>Lorem ipsum dolor sit amet consectetur. Eget mauris ac lacinia pellentesque magna. Nullam diam nulla aliquam convallis.</p><span class="line"></span><span class="avatar" role="img" aria-label="Client portrait"></span><span class="name">Mara Quillen</span></article>
  <article class="quote-card" style="left:784px"><span class="mark">“</span><p>Lorem ipsum dolor sit amet consectetur. Eget mauris ac lacinia pellentesque magna. Nullam diam nulla aliquam convallis.</p><span class="line"></span><span class="avatar" role="img" aria-label="Client portrait"></span><span class="name">Mara Quillen</span></article>
  <a class="btn btn-red" style="left:508px;top:3558px;width:184px;height:46px">More Services</a>
</section>

<section class="contact">
  <h2 class="contact-title">CONTACT US</h2>
  <div class="field" style="top:3750px">Full Name</div>
  <div class="field" style="top:3818px">Phone Number</div>
  <div class="field" style="top:3886px">Email Address</div>
  <div class="field" style="top:3956px;height:150px">Message...</div>
  <a class="btn btn-red" style="left:72px;top:4142px;width:152px;height:44px">Submit Now</a>

  <div class="info">
    <h3>INFORMATION</h3>
    <div class="info-row"><svg width="22" height="22" viewBox="0 0 24 24"><path d="M6.6 10.8a15 15 0 0 0 6.6 6.6l2.2-2.2c.3-.3.7-.4 1-.2 1.1.4 2.3.6 3.6.6.6 0 1 .4 1 1V20c0 .6-.4 1-1 1A17 17 0 0 1 3 4c0-.6.4-1 1-1h3.5c.6 0 1 .4 1 1 0 1.3.2 2.5.6 3.6.1.3 0 .7-.2 1z" fill="#fff"/></svg><div><b>Call</b><span>+1-555-014-2880</span></div></div>
    <div class="info-row"><svg width="22" height="22" viewBox="0 0 24 24"><circle cx="12" cy="12" r="9" fill="none" stroke="#fff" stroke-width="2"/><path d="M8 12l3 3 5-6" fill="none" stroke="#fff" stroke-width="2"/></svg><div><b>Whatsapp</b><span>+1-555-014-2880</span></div></div>
    <div class="info-row"><svg width="22" height="22" viewBox="0 0 24 24"><rect x="2" y="5" width="20" height="14" rx="2" fill="none" stroke="#fff" stroke-width="2"/><path d="M2 6l10 7 10-7" fill="none" stroke="#fff" stroke-width="2"/></svg><div><b>Email</b><span>support@halvardstaffing.example</span></div></div>
    <div class="info-row"><svg width="22" height="22" viewBox="0 0 24 24"><path d="M12 2a7 7 0 0 0-7 7c0 5 7 13 7 13s7-8 7-13a7 7 0 0 0-7-7z" fill="#fff"/><circle cx="12" cy="9" r="2.5" fill="var(--panel)"/></svg><div><b>Location</b><span>Halvardmedia@halvard.example</span></div></div>
  </div>
  <svg class="abs" style="left:668px;top:3708px" width="64" height="64" aria-hidden="true"><polygon points="0,0 64,0 0,64" fill="var(--red)"/></svg>
</section>

<footer class="site-footer">
  <a class="brand"><i></i>Halvard Staffing Solutions</a>
  <nav class="f-nav"><a>Home</a><a>About Us</a><a>Service</a><a>Careers</a><a>Contact</a><a>Testimonial</a></nav>
  <div class="socials"><span></span><span></span><span></span><span></span><span></span></div>
  <p class="f-text">Lorem ipsum dolor sit amet consectetur. Eget mauris ac lacinia pellentesque magna. Nullam diam nulla aliquam convallis. Augue dui ut morbi lacus integer.</p>
  <div class="f-bottom"><span>Copyright © 2025. All Rights Reserved</span><div><a>Privacy Policy</a><a>Terms Of Service</a><a>Cookies Setting</a></div></div>
</footer>

</body>
</html>
```